Letterhead Design Project

Initially, we would like to review our letterheads.

Something simple which uses our corporate imagery well and is nicely balanced.

Please note that I will be following up this letter-head with some customised quote templates and similarly customisable collateral in the next few weeks.

Target Market(s)

Enterprise business

Industry/Entity Type

Quote

Requirements
Must have
• The Nexora9 logo
See www.nexora9.com.au

Our tagline "Enterprise Hosting, Messaging and Server Virtualisation"

Our website address

Ideally in our colour pallette, but will consider submissions which look fantastic and necessitate other colours.

```html
<!DOCTYPE html>
<html lang="en">
<head>
<meta charset="utf-8">
<title>Nexora9 Letterhead</title>
<link rel="stylesheet" href="https://fonts.googleapis.com/css2?family=Arimo:wght@700&family=Open+Sans:wght@400&family=Michroma&display=swap">
<style>
  :root {
    --backdrop: #1c2120;
    --paper: #ffffff;
    --ink: #111111;
    --brand-red: #d0202a;
    --text-grey: #3a3a3a;
    --rule-grey: #b8b8b8;
  }
  * { margin: 0; padding: 0; box-sizing: border-box; }
  html, body {
    width: 960px;
    height: 1200px;
    overflow: hidden;
    background: var(--backdrop);
  }
  .letterhead {
    position: absolute;
    left: 72px;
    top: 72px;
    width: 816px;
    height: 1056px;
    background: var(--paper);
  }
  .brand {
    position: absolute;
    left: 9px;
    top: 8px;
    display: flex;
    align-items: center;
    gap: 8px;
  }
  .brand-square {
    width: 62px;
    height: 62px;
    background: var(--brand-red);
  }
  .brand-name {
    font-family: "Arimo", Arial, sans-serif;
    font-weight: 700;
    font-size: 70px;
    line-height: 1;
    color: var(--ink);
    letter-spacing: -1px;
  }
  .address {
    position: absolute;
    right: 15px;
    top: 34px;
    text-align: right;
    font-family: "Open Sans", sans-serif;
    font-size: 14.5px;
    line-height: 19px;
    color: var(--text-grey);
  }
  .header-rule {
    position: absolute;
    left: 9px;
    top: 78px;
    width: 660px;
    height: 2px;
    background: linear-gradient(to right, rgba(184,184,184,0) 0%, var(--rule-grey) 45%, var(--rule-grey) 70%, rgba(184,184,184,0) 100%);
  }
  .tagline {
    position: absolute;
    left: 11px;
    top: 84px;
    font-family: "Michroma", sans-serif;
    font-size: 9.4px;
    letter-spacing: 1.6px;
    color: var(--ink);
    white-space: nowrap;
  }
  .tagline .cap { font-size: 12px; }
  .contact-footer {
    position: absolute;
    left: 0;
    right: 0;
    top: 1024px;
    text-align: center;
    font-family: "Open Sans", sans-serif;
    font-size: 14.5px;
    color: var(--text-grey);
    word-spacing: 1px;
  }
  .contact-footer .divider { margin: 0 6px; }
</style>
</head>
<body>
  <main class="letterhead">
    <div class="brand">
      <div class="brand-square"></div>
      <div class="brand-name">Nexora9</div>
    </div>
    <address class="address" style="font-style:normal">
      123 Street, Suit #123<br>
      Your City, State 1234
    </address>
    <div class="header-rule"></div>
    <p class="tagline"><span class="cap">E</span>NTERPRISE <span class="cap">H</span>OSTING, <span class="cap">M</span>ESSAGING AND <span class="cap">S</span>ERVER <span class="cap">V</span>IRTUALISATION</p>
    <footer class="contact-footer">
      Ph : 123-123-1234<span class="divider">|</span>Fax : 123-123-1234<span class="divider">|</span>Email : innexora9.com.au<span class="divider">|</span>Web : www.nexora9.com.au
    </footer>
  </main>
</body>
</html>
```